Updated Business Cards

We need to update our business cards to reflect new services and employees. We are a luxury vacation rental company in Sandpoint, Idaho. Would also like to make the front facing font easier to read (larger fonts) I love the original logo created for our company and want to use this for the back of the business card created like before - with the dark blue color. See previous files.

Front of the card needs to include:
Employee Name
Title
Phone: 208-555-0147 (ext X)
Address: 418 W. Larkmoor St, Ste 5
Sandpoint, ID 83871
Book Direct: www.RestWillowbay.example

```html
<!DOCTYPE html>
<html lang="en">
<head>
<meta charset="utf-8">
<title>Halvorsen Management – Business Cards</title>
<link href="https://fonts.googleapis.com/css2?family=Montserrat:wght@400;500;700&display=swap" rel="stylesheet">
<style>
  :root {
    --backdrop: #2a2a2a;
    --card-blue: #0a2a8f;
    --card-blue-light: #1638b4;
    --paper: #f4f4f2;
    --ink-blue: #123a9c;
    --ink-grey: #4a4a4a;
    --rule: #5f6f66;
  }
  html, body {
    margin: 0;
    width: 1200px;
    height: 825px;
    overflow: hidden;
    background: var(--backdrop);
    font-family: "Montserrat", sans-serif;
  }
  .sheet {
    position: relative;
    width: 1200px;
    height: 825px;
  }
  .card {
    position: absolute;
    top: 270px;
    width: 500px;
    height: 286px;
    box-sizing: border-box;
    box-shadow: 0 18px 40px rgba(0,0,0,.45);
  }
  .card-back {
    left: 70px;
    background: linear-gradient(135deg, var(--card-blue), var(--card-blue-light));
    display: flex;
    align-items: center;
    justify-content: center;
  }
  .card-back .wordmark {
    color: #2347c2;
    font-weight: 700;
    font-size: 30px;
    letter-spacing: 2px;
    text-transform: uppercase;
    text-align: center;
    line-height: 1.25;
  }
  .card-front {
    left: 630px;
    background: var(--paper);
    display: flex;
    align-items: center;
    padding: 0 26px 0 24px;
  }
  .brand {
    width: 190px;
    display: flex;
    align-items: center;
    gap: 8px;
  }
  .brand-dot {
    width: 12px;
    height: 12px;
    border-radius: 50%;
    background: var(--ink-blue);
    flex: none;
  }
  .brand-name {
    color: var(--ink-blue);
    font-weight: 700;
    font-size: 17px;
    line-height: 1.2;
    text-transform: uppercase;
    letter-spacing: .5px;
  }
  .divider {
    width: 1px;
    height: 150px;
    background: var(--rule);
    margin: 0 18px 0 10px;
  }
  .contact { color: var(--ink-grey); font-size: 11.5px; line-height: 1.45; }
  .person-name {
    color: var(--ink-blue);
    font-weight: 700;
    font-size: 16px;
    text-transform: uppercase;
    margin: 0;
  }
  .person-title { font-weight: 500; font-size: 12px; margin: 0 0 12px; color: #333; }
  .address { margin: 0 0 10px; }
  .line { display: flex; align-items: center; gap: 7px; margin: 0; }
  .line svg { width: 11px; height: 11px; flex: none; fill: var(--ink-blue); }
</style>
</head>
<body>
<main class="sheet">
  <section class="card card-back">
    <div class="wordmark">Halvorsen<br>Management</div>
  </section>

  <section class="card card-front">
    <div class="brand">
      <span class="brand-dot"></span>
      <span class="brand-name">Halvorsen Management</span>
    </div>
    <div class="divider"></div>
    <div class="contact">
      <p class="person-name">Colin Ashford</p>
      <p class="person-title">Managing Director</p>
      <p class="address">418 W. Larkmoor St, Ste 5<br>Sandpoint, ID 83871</p>
      <p class="line">
        <svg viewBox="0 0 12 12" aria-hidden="true"><path d="M3 0h6a1 1 0 0 1 1 1v10a1 1 0 0 1-1 1H3a1 1 0 0 1-1-1V1a1 1 0 0 1 1-1zm0 1.5v8h6v-8z"/></svg>
        208-555-0147 (ext X)
      </p>
      <p class="line">
        <svg viewBox="0 0 12 12" aria-hidden="true"><path d="M0 2h12v1.2L6 7 0 3.2zM0 4.6l6 3.8 6-3.8V10H0z"/></svg>
        info@RestWillowbay.example
      </p>
      <p class="line">
        <svg viewBox="0 0 12 12" aria-hidden="true"><circle cx="6" cy="6" r="6"/></svg>
        www.RestWillowbay.example
      </p>
    </div>
  </section>
</main>
</body>
</html>
```